Modern and Exciting Real Estate Yard Sign

We are looking for a new and exciting design for our real estate property listing yard signs. We would like our signs to be custom with pictures of the property included. We are not looking for the plain old standard designs.

I have attached a copy of our current design and the logo to be used.

Target Market(s)

Home Buyers

Industry/Entity Type

Real Estate

Font styles to use
Sans Serif
Other font styles liked:
• Our company font is Trajan Pro

Colors

Designer to choose colors to be used in the design.

Requirements
Must have
• We would like to include 4 images of the property being advertised, which is one large main picture and 3 smaller accent pictures. We must also have somewhere to spotlight/add an agent headshot and contact information.
• Must include logos for Fair Dwelling Access Pledge and Homewright which are also included.
• Dimensions should be 2' wide by 4' tall and 300 dpi. Files MUST be easily/quickly editable as we will be creating new signs using this template for various properties.
Should not have
• We are basically trying to stay away from any of the traditional boring signs like most of these:
• https://www.findlumo.net/query?q=realtor+yard+signs&source=lnms&tbm=isch&sa=X&ved=0bhVLFxk8q6Ev19EUBiWn3JNLIbmPKIbnOC4lR_BVJDDhC&biw=1282&bih=1293

```html
<!DOCTYPE html>
<html lang="en">
<head>
<meta charset="utf-8">
<title>Silver Alder Real Estate – For Sale Yard Sign</title>
<link href="https://fonts.googleapis.com/css2?family=Cinzel:wght@400;500;600;700&display=swap" rel="stylesheet">
<style>
  :root {
    --page-bg: #e9e6e1;
    --ink: #3a3a3a;
    --band-dark: #464646;
    --panel-light: #efefef;
    --silver-a: #ffffff;
    --silver-b: #b5b5b5;
    --frame-white: #ffffff;
  }
  * { box-sizing: border-box; margin: 0; padding: 0; }
  html, body {
    width: 850px; height: 1200px; overflow: hidden;
    background: var(--page-bg);
  }
  .canvas { position: relative; width: 850px; height: 1200px; }
  .yard-sign {
    position: absolute; left: 164px; top: 78px;
    width: 522px; height: 1044px;
    background: var(--panel-light);
    overflow: hidden;
    font-family: "Cinzel", "Times New Roman", serif;
    color: var(--ink);
  }
  .header-art { position: absolute; left: 0; top: 0; width: 522px; height: 603px; }

  .brand { position: absolute; left: 0; width: 100%; text-align: center; }
  .brand-dot {
    position: absolute; top: 12px; left: 50%; margin-left: -38px;
    width: 76px; height: 76px; border-radius: 50%; background: var(--ink);
  }
  .brand-name {
    position: absolute; top: 94px; left: 0; width: 100%;
    font-size: 30px; font-weight: 400; line-height: 1; letter-spacing: 0.5px;
  }
  .brand-tag {
    position: absolute; top: 125px; left: 0; width: 100%;
    font-size: 13px; font-weight: 400; line-height: 1; letter-spacing: 3px;
  }

  .for-sale-band {
    position: absolute; top: 602px; left: 0; width: 100%; height: 110px;
    background: var(--band-dark);
    display: flex; align-items: center; justify-content: center;
  }
  .for-sale-band h1 {
    font-size: 94px; font-weight: 400; letter-spacing: 2px; line-height: 1;
    margin-top: 4px;
    background: linear-gradient(180deg, var(--silver-a) 15%, var(--silver-b) 95%);
    -webkit-background-clip: text; background-clip: text; color: transparent;
  }

  .gallery-frame {
    position: absolute; top: 717px;
    width: 158px; height: 120px; background: var(--frame-white);
    padding: 9px;
  }
  .gallery-frame.one { left: 10px; }
  .gallery-frame.two { left: 183px; }
  .gallery-frame.three { left: 355px; }
  .gallery-frame div { width: 100%; height: 100%; }
  .photo-bedroom { background: linear-gradient(180deg, #e9e4dc 0%, #cfc6bb 40%, #7d5a46 62%, #b3aba2 100%); }
  .photo-kitchen { background: linear-gradient(180deg, #f3f1ed 0%, #c9a06d 35%, #3e3a36 55%, #d9d3c9 100%); }
  .photo-bath { background: linear-gradient(180deg, #ece7df 0%, #dcd3c6 45%, #c59a66 75%, #b88d5d 100%); }

  .line { position: absolute; left: 0; width: 100%; text-align: center; line-height: 1; }
  .contact-lead { top: 843px; font-size: 23px; font-weight: 500; letter-spacing: 0.5px; }
  .contact-rule {
    position: absolute; top: 866px; left: 43px;
    width: 436px; height: 3px; background: var(--band-dark);
  }
  .visit-tag {
    position: absolute; top: 878px; left: 168px;
    width: 186px; height: 23px;
    background: var(--band-dark); color: #fff;
    font-size: 16px; font-weight: 700; letter-spacing: 0.5px; line-height: 23px;
    text-align: center;
    clip-path: polygon(7% 0, 100% 0, 93% 100%, 0 100%);
  }
  .contact-web { top: 911px; font-size: 26px; font-weight: 400; }
  .contact-name { top: 940px; font-size: 29px; font-weight: 600; }
  .contact-email {
    top: 975px; font-size: 15px; font-weight: 400;
    display: flex; align-items: center; justify-content: center; gap: 4px;
  }
  .contact-phone {
    top: 998px; font-size: 29px; font-weight: 700;
    display: flex; align-items: center; justify-content: center; gap: 10px;
  }
</style>
</head>
<body>
<main class="canvas">
  <section class="yard-sign">
    <svg class="header-art" viewBox="0 0 522 603" width="522" height="603">
      <defs>
        <linearGradient id="topPanel" x1="0" y1="0" x2="1" y2="1">
          <stop offset="0" stop-color="#c8c8c8"/>
          <stop offset="0.5" stop-color="#f3f3f3"/>
          <stop offset="1" stop-color="#c0c0c0"/>
        </linearGradient>
        <linearGradient id="housePhoto" x1="0" y1="0" x2="0" y2="1">
          <stop offset="0" stop-color="#5fa6e6"/>
          <stop offset="0.3" stop-color="#a8cfee"/>
          <stop offset="0.42" stop-color="#7f97a2"/>
          <stop offset="0.65" stop-color="#6a8272"/>
          <stop offset="0.85" stop-color="#4e8f3a"/>
          <stop offset="1" stop-color="#62ad45"/>
        </linearGradient>
      </defs>
      <rect x="0" y="0" width="522" height="603" fill="url(#topPanel)"/>
      <polygon class="chevron-band" fill="#464646"
        points="0,256 261,147 522,256 522,284 261,172 0,284"/>
      <polygon class="hero-photo" role="img"
        aria-label="Main listing photo: two-storey grey-green craftsman house with gabled roofs, trimmed shrubs and green lawn under blue sky"
        fill="url(#housePhoto)"
        points="0,290 261,177 522,290 522,603 0,603"/>
      <polyline fill="none" stroke="#ffffff" stroke-width="5"
        points="0,288 261,175 522,288"/>
      <rect x="425" y="563" width="27" height="27" rx="2" fill="#3a3a3a"
        role="img" aria-label="Fair Dwelling Access Pledge badge"/>
      <rect x="471" y="563" width="27" height="27" rx="2" fill="#3a3a3a"
        role="img" aria-label="Homewright badge"/>
    </svg>

    <header class="brand">
      <span class="brand-dot"></span>
      <div class="brand-name">SILVER ALDER</div>
      <div class="brand-tag">REAL ESTATE</div>
    </header>

    <div class="for-sale-band"><h1>FOR SALE</h1></div>

    <div class="gallery-frame one"><div class="photo-bedroom" role="img" aria-label="Master bedroom with wooden bed and carpet"></div></div>
    <div class="gallery-frame two"><div class="photo-kitchen" role="img" aria-label="Kitchen with oak cabinets and steel appliances"></div></div>
    <div class="gallery-frame three"><div class="photo-bath" role="img" aria-label="Bathroom with soaking tub and double vanity"></div></div>

    <p class="line contact-lead">FOR ADDITIONAL INFORMATION</p>
    <div class="contact-rule"></div>
    <span class="visit-tag">PLEASE VISIT</span>
    <p class="line contact-web">WWW.HARBORLISTINGS.COM</p>
    <p class="line contact-name">DANIEL MARSH, BROKER</p>
    <p class="line contact-email">
      <svg width="18" height="18" viewBox="0 0 20 20" aria-hidden="true">
        <circle cx="10" cy="10" r="9" fill="none" stroke="#3a3a3a" stroke-width="1.6"/>
        <rect x="5" y="6.5" width="10" height="7" fill="none" stroke="#3a3a3a" stroke-width="1.4"/>
        <polyline points="5,6.5 10,10.5 15,6.5" fill="none" stroke="#3a3a3a" stroke-width="1.4"/>
      </svg>
      DANIEL@SILVERALDERHOMES.COM
    </p>
    <p class="line contact-phone">
      <svg width="32" height="32" viewBox="0 0 30 30" aria-hidden="true">
        <circle cx="15" cy="15" r="14" fill="#3a3a3a"/>
        <path d="M8 12c0-2 2-3 7-3s7 1 7 3v1h-3v-1.5h-8V13H8z" fill="#fff"/>
        <rect x="10" y="14" width="10" height="7" rx="1.5" fill="#fff"/>
        <circle cx="15" cy="17.5" r="1.8" fill="#3a3a3a"/>
      </svg>
      (555) 014-2290 (OFFICE)
    </p>
  </section>
</main>
</body>
</html>
```